Larkmoor Apartments Downtown Northport

We are looking to redesign our entry way sign at Larkmoor Apartments, a low density residential apartment building, located in Downtown Northport, Alabama, U.S. Downtown Northport is a bustling boutique business district with a small town feel comprised of shops, restaurants, and a renowned arts community known for Velloway Arts Center and Festival which is one of the nation's top outdoor arts festivals. Larkmoor Apartments and its sign is the first thing you seen when you enter Downtown Northport. We are looking to redesign our sign, entry way and landscaping to compliment the building and character of the historic downtown.

Target Market(s)

Our apartment building is comprised of 20 apartments units with tenants who are primarily part of the local workforce, young professionals, or students at the Tressdale University or other nearby institutions.

Requirements
Must have
• The name of the apartment building - Larkmoor
Phone number on the sign 205-555-0148

```html
<!DOCTYPE html>
<html lang="en">
<head>
<meta charset="utf-8">
<title>Larkmoor Apartments – Entry Sign</title>
<link href="https://fonts.googleapis.com/css2?family=Teko:wght@500&display=swap" rel="stylesheet">
<style>
  :root {
    --backdrop: #e2e2df;
    --sign-face: #f3f3f2;
    --sign-face-shade: #e9e9e8;
    --ink-brown: #7b5736;
  }
  html, body {
    margin: 0;
    padding: 0;
    width: 1200px;
    height: 794px;
    overflow: hidden;
    background: var(--backdrop);
  }
  .canvas {
    position: relative;
    width: 1200px;
    height: 794px;
  }
  .sign-face {
    position: absolute;
    left: 30px;
    top: 135px;
    width: 1140px;
    height: 524px;
    background: linear-gradient(90deg, var(--sign-face) 0%, var(--sign-face-shade) 50%, var(--sign-face) 100%);
    box-shadow: 0 2px 6px rgba(0,0,0,0.12);
  }
  .sign-art {
    display: block;
    width: 100%;
    height: 100%;
  }
  .building-name,
  .phone-number {
    font-family: "Teko", sans-serif;
    font-weight: 500;
    fill: var(--ink-brown);
  }
  .building-name {
    font-size: 230px;
  }
  .phone-number {
    font-size: 85px;
  }
</style>
</head>
<body>
  <main class="canvas">
    <section class="sign-face" aria-label="Larkmoor Apartments entry sign">
      <svg class="sign-art" viewBox="0 0 1140 524" xmlns="http://www.w3.org/2000/svg">
        <text class="building-name" x="68" y="319" textLength="1004" lengthAdjust="spacingAndGlyphs">LARKMOOR</text>
        <text class="phone-number" x="701" y="443" textLength="372" lengthAdjust="spacingAndGlyphs">205-555-0148</text>
      </svg>
    </section>
  </main>
</body>
</html>
```